Package design for Mica powder sachets

Our mica powder product comes in two sets of colors, a set of 60 and 35 packed inside sachet bags individually. This project will require two sizes of the packing box , one for the set of 60 and other for 35. We do not have a specific design requirement as long as the design reflects the theme of our product. Box diagram for both sizes is attached together with color chart, content, logo, sachet design and sample of a packaging design we like. The content is the same for both sizes accept for number of colors included.

```html
<!DOCTYPE html>
<html lang="en">
<head>
<meta charset="utf-8">
<title>Birchwell Crafts – Mica Powder Box Dieline</title>
<link href="https://fonts.googleapis.com/css2?family=Open+Sans:ital,wght@0,400;0,600;0,700;0,800;1,400&display=swap" rel="stylesheet">
<style>
:root{
  --ink:#1f1d1e;
  --panel-line:#4a4748;
  --gold-a:#cfa94a;
  --gold-b:#e6c262;
  --red:#d3302f;
  --red-b:#ef5a3a;
  --cream:#ffffff;
  --gold-text:#e2b84a;
  --row:#3b393a;
  --row-line:#8a8788;
  --paper:#ffffff;
  --halo-a:#6a4a78;
  --halo-b:#3f5a6e;
}
*{margin:0;padding:0;box-sizing:border-box}
html,body{width:1200px;height:1088px;overflow:hidden;background:var(--paper)}
body{font-family:"Open Sans",sans-serif;color:var(--cream)}
.dieline{position:relative;width:1200px;height:1088px}
.dieline svg.shapes{position:absolute;left:0;top:0}
.brand{position:absolute;text-align:center;font-family:"Open Sans",sans-serif;font-weight:700;color:var(--cream);line-height:1.05;letter-spacing:.5px}
.brand span{display:block}
.color-chart{position:absolute;left:407px;top:190px;display:flex;gap:1px}
.chart-col{width:134px;border-collapse:collapse;font-size:7px;background:var(--row)}
.chart-col:last-child{width:122px}
.chart-col th{height:18px;background:linear-gradient(90deg,var(--red),var(--red-b));font-weight:600;font-size:7.5px;color:#1d1b1c;text-align:left;padding-left:4px}
.chart-col th.num{width:26px}
.chart-col td{height:11.6px;border:0.5px solid var(--row-line);padding:0 3px;white-space:nowrap;color:#f1f1f1}
.chart-col td:first-child{text-align:center}
.info{position:absolute;left:407px;top:365px;font-size:7.5px;line-height:1.45}
.info .headline{color:var(--gold-text);font-weight:700;font-size:8.8px}
.info .uses{color:var(--gold-text);font-style:italic;font-size:8.5px;margin-bottom:1px}
.info .label{color:var(--red);font-weight:700}
.info .web{padding-left:38px;font-size:7.2px;line-height:1.3}
.info .web i{display:block}
.blank-box{position:absolute;left:668px;top:367px;width:126px;height:43px;border:1px solid #e8e8e8}
.item-box{position:absolute;left:603px;top:420px;width:191px;height:16px;border:1px solid #e8e8e8;font-size:7.8px;padding-left:7px;line-height:14px}
.mica-title{position:absolute;left:561px;top:781px;font-weight:700;font-size:22px;line-height:29px;color:var(--cream)}
.contents-line{position:absolute;left:561px;top:853px;font-size:10px;color:var(--cream)}
.badge-num{font-family:"Open Sans",sans-serif;font-weight:800;fill:var(--red)}
.badge-word{font-family:"Open Sans",sans-serif;font-weight:700;fill:#2a2728}
.band-text{font-family:"Open Sans",sans-serif;font-weight:700;fill:var(--cream)}
</style>
</head>
<body>
<div class="dieline">
<svg class="shapes" width="1200" height="1088" viewBox="0 0 1200 1088">
  <defs>
    <linearGradient id="gold" x1="0" x2="1" y1="0" y2="0">
      <stop offset="0" stop-color="var(--gold-a)"/><stop offset=".5" stop-color="var(--gold-b)"/><stop offset="1" stop-color="var(--gold-a)"/>
    </linearGradient>
    <radialGradient id="goldDisc" cx=".4" cy=".35" r=".7">
      <stop offset="0" stop-color="#ecc96a"/><stop offset="1" stop-color="#c9a045"/>
    </radialGradient>
    <linearGradient id="band" x1="0" x2="1">
      <stop offset="0" stop-color="var(--red)"/><stop offset="1" stop-color="#cc4b36"/>
    </linearGradient>
    <linearGradient id="halo" x1="0" x2="1" y1="0" y2="1">
      <stop offset="0" stop-color="var(--halo-a)"/><stop offset="1" stop-color="var(--halo-b)"/>
    </linearGradient>
  </defs>
  <g stroke="var(--panel-line)" stroke-width=".8">
    <rect class="lid-flap" x="375" y="0" width="450" height="162" fill="var(--ink)"/>
    <path class="ear" d="M375,0 L300,0 C240,0 195,60 188,120 C185,150 205,162 230,162 L375,162Z" fill="url(#gold)" stroke="#333"/>
    <path class="ear" d="M825,0 L900,0 C960,0 1005,60 1012,120 C1015,150 995,162 970,162 L825,162Z" fill="url(#gold)" stroke="#333"/>
    <path class="wing" d="M375,163 L223,193 C200,198 188,215 188,240 L188,385 C188,410 200,420 223,424 L375,462Z" fill="var(--ink)"/>
    <path class="wing" d="M825,163 L977,193 C1000,198 1012,215 1012,240 L1012,385 C1012,410 1000,420 977,424 L825,462Z" fill="var(--ink)"/>
    <rect class="lid" x="375" y="162" width="450" height="300" fill="var(--ink)" stroke="var(--red)"/>
    <rect x="375" y="462" width="450" height="162" fill="var(--ink)"/>
    <rect class="tuck" x="225" y="464" width="150" height="158" fill="url(#gold)" stroke="#333"/>
    <rect class="tuck" x="825" y="465" width="149" height="157" fill="url(#gold)" stroke="#333"/>
    <rect x="0" y="624" width="187" height="301" fill="var(--ink)"/>
    <rect x="187" y="624" width="188" height="301" fill="var(--ink)"/>
    <rect x="375" y="624" width="450" height="301" fill="var(--ink)"/>
    <rect x="825" y="624" width="187" height="301" fill="var(--ink)"/>
    <rect x="1012" y="624" width="188" height="301" fill="var(--ink)"/>
    <rect x="225" y="927" width="150" height="161" fill="var(--ink)"/>
    <rect x="375" y="925" width="450" height="163" fill="var(--ink)"/>
    <rect x="825" y="927" width="149" height="161" fill="var(--ink)"/>
  </g>

  <!-- front badge and band -->
  <rect x="539" y="775" width="286" height="66" fill="url(#band)"/>
  <circle cx="491" cy="809" r="71" fill="url(#halo)" role="img" aria-label="Decorative ring of colourful dots around the badge"/>
  <circle cx="491" cy="809" r="56" fill="url(#goldDisc)"/>
  <text class="badge-num" x="491" y="826" font-size="58" text-anchor="middle">35</text>
  <text class="badge-word" x="491" y="842" font-size="13" text-anchor="middle">INSPIRING</text>

  <!-- left side panel -->
  <rect x="268" y="808" width="27" height="117" fill="url(#band)"/>
  <g transform="translate(281,789) rotate(90)">
    <circle r="30" fill="url(#halo)" role="img" aria-label="Decorative ring of colourful dots around the badge"/>
    <circle r="23" fill="url(#goldDisc)"/>
    <text class="badge-num" x="0" y="8" font-size="23" text-anchor="middle">35</text>
    <text class="badge-word" x="0" y="15" font-size="5" text-anchor="middle">INSPIRING</text>
  </g>
  <g transform="translate(281,866) rotate(90)">
    <text class="band-text" x="0" y="-2" font-size="8.5" text-anchor="middle">MICA POWDER</text>
    <text class="band-text" x="-12" y="8" font-size="8.5" text-anchor="middle">COLORS</text>
  </g>
  <g transform="translate(280,688) rotate(90)">
    <text class="band-text" x="0" y="-2" font-size="14" text-anchor="middle">Birchwell</text>
    <text class="band-text" x="0" y="13" font-size="14" text-anchor="middle">Crafts</text>
  </g>

  <!-- right side panel -->
  <rect x="905" y="624" width="26" height="116" fill="url(#band)"/>
  <g transform="translate(918,683) rotate(-90)">
    <text class="band-text" x="0" y="-2" font-size="8.5" text-anchor="middle">MICA POWDER</text>
    <text class="band-text" x="-12" y="8" font-size="8.5" text-anchor="middle">COLORS</text>
  </g>
  <g transform="translate(918,762) rotate(-90)">
    <circle r="30" fill="url(#halo)" role="img" aria-label="Decorative ring of colourful dots around the badge"/>
    <circle r="23" fill="url(#goldDisc)"/>
    <text class="badge-num" x="0" y="8" font-size="23" text-anchor="middle">35</text>
    <text class="badge-word" x="0" y="15" font-size="5" text-anchor="middle">INSPIRING</text>
  </g>
  <g transform="translate(920,860) rotate(-90)">
    <text class="band-text" x="0" y="-2" font-size="14" text-anchor="middle">Birchwell</text>
    <text class="band-text" x="0" y="13" font-size="14" text-anchor="middle">Crafts</text>
  </g>
</svg>

<div class="brand" style="left:475px;top:522px;width:250px;font-size:22px"><span>Birchwell</span><span>Crafts</span></div>
<div class="brand" style="left:450px;top:650px;width:300px;font-size:29px"><span>Birchwell</span><span>Crafts</span></div>
<div class="brand" style="left:475px;top:985px;width:250px;font-size:22px"><span>Birchwell</span><span>Crafts</span></div>

<div class="color-chart">
  <table class="chart-col">
    <tr><th class="num"></th><th>Name</th><th>No</th></tr>
    <tr><td>1)</td><td>Sage Glow</td><td>M2</td></tr>
    <tr><td>2)</td><td>Pearl White</td><td>M6</td></tr>
    <tr><td>3)</td><td>Light Gold</td><td>M7</td></tr>
    <tr><td>4)</td><td>Yellow Gold</td><td>M9</td></tr>
    <tr><td>5)</td><td>Glitzy Gold</td><td>M13</td></tr>
    <tr><td>6)</td><td>Citrus Zest</td><td>M16</td></tr>
    <tr><td>7)</td><td>Lemon Twist</td><td>M18</td></tr>
    <tr><td>8)</td><td>Charcoal</td><td>M21</td></tr>
    <tr><td>9)</td><td>Space Gray</td><td>M22</td></tr>
    <tr><td>10)</td><td>Chocolate Brown</td><td>M21</td></tr>
    <tr><td>11)</td><td>Bronze</td><td>M24</td></tr>
    <tr><td>12)</td><td>Golden Brown</td><td>M27</td></tr>
  </table>
  <table class="chart-col">
    <tr><th class="num"></th><th>Name</th><th>No</th></tr>
    <tr><td>13)</td><td>Jungle Green</td><td>M29</td></tr>
    <tr><td>14)</td><td>Turquoise</td><td>M31</td></tr>
    <tr><td>15)</td><td>Mint Green</td><td>M32</td></tr>
    <tr><td>16)</td><td>Emerald Green</td><td>M35</td></tr>
    <tr><td>17)</td><td>Spring Green</td><td>M36</td></tr>
    <tr><td>18)</td><td>Sky Blue</td><td>M40</td></tr>
    <tr><td>19)</td><td>Denim Blue</td><td>M43</td></tr>
    <tr><td>20)</td><td>Bright Blue</td><td>M45</td></tr>
    <tr><td>21)</td><td>Sapphire Blue</td><td>M47</td></tr>
    <tr><td>22)</td><td>Navy Blue</td><td>M49</td></tr>
    <tr><td>23)</td><td>Violet Purple</td><td>M53</td></tr>
    <tr><td>24)</td><td>Lavinder</td><td>M55</td></tr>
  </table>
  <table class="chart-col">
    <tr><th class="num"></th><th>Name</th><th>No</th></tr>
    <tr><td>25)</td><td>Coral Orange</td><td>M57</td></tr>
    <tr><td>26)</td><td>Rose Red</td><td>M59</td></tr>
    <tr><td>27)</td><td>Raspberry</td><td>M62</td></tr>
    <tr><td>28)</td><td>Rose Pink</td><td>M67</td></tr>
    <tr><td>29)</td><td>Hot Pink</td><td>M70</td></tr>
    <tr><td>30)</td><td>Creamy Pink</td><td>M73</td></tr>
    <tr><td>31)</td><td>Burgandy</td><td>M74</td></tr>
    <tr><td>32)</td><td>Copper</td><td>M75</td></tr>
    <tr><td>33)</td><td>Burnt Orange</td><td>M77</td></tr>
    <tr><td>34)</td><td>Brilliant Silver</td><td>M78</td></tr>
    <tr><td>35)</td><td>Olive Green</td><td>M80</td></tr>
    <tr><td></td><td></td><td></td></tr>
  </table>
</div>

<div class="info">
  <div class="headline">Multi-purpose, Cosmetic Grade Non-toxic, Premium Colors</div>
  <div class="uses">For Epoxy Resin, Soap, Slime, Candles, Paint And Much More</div>
  <div><span class="label">contents:</span> 60 Colors, 3 Measuring Spoons, User Guide</div>
  <div><span class="label">warning :</span> Choking Hazard - Small Parts. Not For Children Under 3 Years.</div>
  <div class="web"><i>www.shopbirchwell.com</i>for more products and and information</div>
</div>
<div class="blank-box"></div>
<div class="item-box">Item No:</div>

<div class="mica-title">MICA POWDER<br>COLORS</div>
<div class="contents-line">60 X 5g (0.18 oz) Includes 3 measuring spoons</div>
</div>
</body>
</html>
```